Vexorun.co is a multi-sport platform that connects players, clubs, coaches, and organizers in one ecosystem.

Core value:
- Players can instantly find or create games across sports (padel, pickleball, tennis, soccer, etc.)
- Clubs can manage players, classes, staff, and tournaments in one place
- Coaches and organizers can create events and earn money directly through the platform

Key differentiator:
Vexorun is not just for finding games — it is a revenue engine for clubs and sports communities.

Main features to highlight:
- Find and join games instantly
- Create games without coordination friction
- Club management (players, classes, payments)
- Coaches offering lessons and programs
- Tournaments and events between clubs
- Fill empty court time with automated or quick-created events

Business model:
- Free to join
- Platform takes a small fee on transactions (events, classes, subscriptions)

Tagline:
“Let the Games Begin & Pick Your Challenge”

Tone:
Modern, premium, community-driven, and action-oriented.
Focus on simplicity, energy, and real usage scenarios.

Target Market(s)

multi-sport platform that connects players, clubs, coaches, and organizers in one ecosystem.

Industry/Entity Type

Sport

Coding

Coded - Design and coding required

Number of Pages Required

3 page

Requirements
Must have
• Build you the exact Webflow structure (class-by-class export)
Nice to have
• Html y css

```html
<!DOCTYPE html>
<html lang="en">
<head>
<meta charset="utf-8">
<title>Vexorun — Let the Games Begin</title>
<link rel="stylesheet" href="https://fonts.googleapis.com/css2?family=Oswald:wght@500;600;700&family=Poppins:wght@400;500;600;700&display=swap">
<style>
:root{
  --bg:#1c1c1c;
  --bg-deep:#141714;
  --card:#232323;
  --card-line:#343434;
  --text:#ffffff;
  --muted:#b9b9b9;
  --lime:#9fd236;
  --green:#5fae2e;
  --green-dark:#2f7d22;
  --head:'Oswald',sans-serif;
  --body:'Poppins',sans-serif;
}
*{box-sizing:border-box;margin:0;padding:0}
html,body{width:1200px;height:5029px;overflow:hidden}
body{background:var(--bg);color:var(--text);font-family:var(--body);position:relative}
.section{position:absolute;left:0;width:1200px;overflow:hidden}
.abs{position:absolute}
.eyebrow{position:absolute;left:0;width:1200px;text-align:center;font:500 13px var(--body);color:var(--lime);text-transform:uppercase;letter-spacing:.3px}
.title{position:absolute;left:0;width:1200px;text-align:center;font:700 36px/42px var(--head);text-transform:uppercase;letter-spacing:.3px}
.title-bar{position:absolute;left:560px;width:80px;height:4px;border-radius:2px;background:var(--lime)}
/* buttons */
.btn{position:absolute;display:flex;align-items:center;justify-content:space-between;height:42px;border-radius:21px;padding:0 5px 0 20px;font:600 13px var(--body);text-transform:uppercase;white-space:nowrap}
.btn .arr{width:32px;height:32px;border-radius:50%;display:flex;align-items:center;justify-content:center}
.btn-green{background:linear-gradient(90deg,var(--lime),var(--green));color:#fff}
.btn-green .arr{background:#fff}
.btn-outline{border:2px solid var(--lime);color:#fff;background:rgba(0,0,0,.3)}
.btn-outline .arr{background:#fff}
.btn-white{background:#fff;color:#1c1c1c}
.btn-white .arr{background:var(--green)}
.btn-dark{background:#1c1c1c;color:#fff}
.btn-dark .arr{background:#fff}
/* logo */
.brand{position:absolute;display:flex;align-items:center;gap:10px;font:600 30px var(--body);color:#fff}
.brand-dot{width:58px;height:58px;border-radius:50%;background:var(--green)}
/* flags */
.flags{position:absolute;display:flex;flex-wrap:wrap;gap:10px 12px}
.flag{display:flex;flex-direction:column;align-items:center;gap:3px;font:400 7px var(--body);color:var(--muted);width:40px}
.flag i{display:block;width:26px;height:17px;border-radius:2px}
.f-uk{background:linear-gradient(#c8102e,#c8102e) center/100% 22% no-repeat,linear-gradient(#c8102e,#c8102e) center/18% 100% no-repeat,linear-gradient(#fff,#fff) center/100% 38% no-repeat,linear-gradient(#fff,#fff) center/30% 100% no-repeat,#012169}
.f-es{background:linear-gradient(#c60b1e 25%,#ffc400 25% 75%,#c60b1e 75%)}
.f-lu{background:linear-gradient(#ed2939 33%,#fff 33% 66%,#00a1de 66%)}
.f-jp{background:radial-gradient(circle,#bc002d 28%,#fff 30%)}
.f-ru{background:linear-gradient(#fff 33%,#0039a6 33% 66%,#d52b1e 66%)}
.f-kr{background:radial-gradient(circle,#cd2e3a 24%,#fff 26%)}
.f-ca{background:radial-gradient(circle,#d52b1e 14%,transparent 16%),linear-gradient(90deg,#d52b1e 25%,#fff 25% 75%,#d52b1e 75%)}
.f-us{background:linear-gradient(#3c3b6e,#3c3b6e) top left/45% 54% no-repeat,repeating-linear-gradient(#b22234 0 1.3px,#fff 1.3px 2.6px)}
.f-cz{background:linear-gradient(to right,#11457e 32%,transparent 32%),linear-gradient(#fff 50%,#d7141a 50%)}
.f-br{background:radial-gradient(circle,#002776 20%,#ffdf00 22% 42%,#009c3b 44%)}
.f-pr{background:linear-gradient(to right,#0050f0 35%,transparent 35%),repeating-linear-gradient(#ed0000 0 3.4px,#fff 3.4px 6.8px)}
.f-cr{background:linear-gradient(#002b7f 17%,#fff 17% 33%,#ce1126 33% 67%,#fff 67% 83%,#002b7f 83%)}
.f-cn{background:radial-gradient(circle at 25% 30%,#ffde00 12%,#de2910 14%)}
.f-in{background:radial-gradient(circle,#000080 10%,transparent 12%),linear-gradient(#ff9933 33%,#fff 33% 66%,#138808 66%)}
/* hero */
.hero{top:0;height:628px;background:radial-gradient(ellipse at 45% 35%,#3b4a34 0%,#1e261b 45%,#121511 100%)}
.hero-photo{position:absolute;inset:0;background:radial-gradient(ellipse 260px 320px at 560px 300px,rgba(90,110,70,.45),transparent 70%),linear-gradient(180deg,transparent 70%,rgba(40,80,30,.5))}
.nav-actions .btn{height:44px;top:20px}
.hero-title{position:absolute;left:105px;top:165px;font:700 38px/58px var(--body);color:#fff}
.hero-title span{color:var(--lime);display:block}
.hero-sub{position:absolute;left:105px;top:290px;font:400 14px/25px var(--body);width:420px}
.hero-note{position:absolute;left:105px;top:446px;font:500 11px var(--body)}
.phones{position:absolute;border-radius:36px;background:linear-gradient(160deg,#2b3330,#111614 60%,#0c0f0d);border:3px solid #2c2c2c;box-shadow:0 20px 50px rgba(0,0,0,.6)}
/* sports */
.sports{top:628px;height:377px;background:var(--bg)}
.sport-card{position:absolute;top:176px;width:170px;height:107px;border-radius:8px;background:#2a2a2a;border:1px solid #3a3a3a;display:flex;flex-direction:column;align-items:center;justify-content:flex-end;padding-bottom:16px;font:600 15px var(--head);text-transform:uppercase;letter-spacing:.5px}
.sport-card svg{margin-bottom:8px}
/* one place */
.oneplace{top:1005px;height:800px;background:radial-gradient(ellipse at 50% 100%,#2c3327,#191c18 60%,#161616)}
.oneplace-visual{position:absolute;left:130px;top:156px;width:900px;height:350px;border-radius:12px;background:radial-gradient(ellipse at 20% 50%,rgba(140,90,60,.35),transparent 45%),radial-gradient(ellipse at 65% 50%,rgba(40,60,55,.8),transparent 60%)}
.sub-head{position:absolute;font:600 18px var(--head);text-transform:uppercase;letter-spacing:.4px}
.mini-card{position:absolute;top:605px;height:121px;border-radius:8px;background:rgba(40,40,40,.85);border:1px solid var(--card-line)}
.mini-card .ico{position:absolute;left:12px;top:18px;width:42px;height:42px;border-radius:6px;background:linear-gradient(135deg,var(--lime),var(--green));display:flex;align-items:center;justify-content:center}
.mini-card p{position:absolute;left:16px;top:84px;font:500 12px var(--body)}
/* features */
.features{top:1805px;height:800px;background:var(--bg)}
.feat{position:absolute;width:289px;height:207px;border-radius:8px;background:var(--card);border:1px solid var(--card-line);text-align:center;padding:96px 22px 0}
.feat svg{position:absolute;left:50%;top:26px;transform:translateX(-50%)}
.feat h3{font:600 14px/18px var(--body);margin-bottom:4px}
.feat p{font:400 11.5px/19px var(--body);color:var(--muted)}
/* how */
.how{top:2605px;height:566px;background:radial-gradient(ellipse 260px 140px at 600px 520px,#3c3c3c,transparent 70%),linear-gradient(180deg,#181818,#131313 60%,#222)}
.step{position:absolute;top:186px;width:240px;text-align:center}
.step .num{width:34px;height:34px;border-radius:50%;margin:0 auto 12px;background:var(--green);border:3px solid var(--lime);font:600 13px/28px var(--body)}
.step h3{font:600 15px var(--body);margin-bottom:4px}
.step p{font:400 12px/19px var(--muted);font-family:var(--body);color:var(--muted)}
.step-line{position:absolute;top:203px;left:280px;width:660px;height:1px;border-top:1px dashed #555}
.ball{position:absolute;left:525px;top:420px;width:150px;height:150px;border-radius:50%;background:radial-gradient(circle at 45% 35%,#5a5a5a,#1a1a1a 70%)}
/* built for */
.builtfor{top:3171px;height:523px;background:var(--bg)}
.role{position:absolute;top:282px;width:289px;height:166px;border-radius:8px;background:var(--card);border:1px solid var(--card-line);text-align:center;padding-top:70px}
.role.active{background:linear-gradient(180deg,var(--lime),var(--green-dark));border:none}
.role .badge{position:absolute;left:50%;top:-46px;transform:translateX(-50%);width:94px;height:94px;border-radius:50%;background:linear-gradient(135deg,var(--lime),var(--green));border:6px solid #2a2a2a;display:flex;align-items:center;justify-content:center}
.role h3{font:600 17px var(--body);margin-bottom:8px}
.role p{font:400 12px/18px var(--body);color:var(--muted)}
.role.active p{color:#eef6e5}
/* launch */
.launch{top:3694px;height:559px;background:linear-gradient(180deg,#1c1c1c,#181a18)}
.launch-title{position:absolute;left:140px;top:116px;font:700 36px/41px var(--head);text-transform:uppercase}
.check{position:absolute;left:140px;display:flex;align-items:center;gap:7px;font:500 12px var(--body)}
.check i{width:12px;height:12px;border-radius:50%;background:var(--lime);display:flex;align-items:center;justify-content:center}
.flag-box{position:absolute;left:140px;top:358px;width:344px;height:100px;border-radius:8px;background:#242424;border:1px solid var(--card-line)}
.map{position:absolute;left:558px;top:104px;width:521px;height:350px;border-radius:40%;background:radial-gradient(ellipse at 30% 40%,#2f7d22,transparent 55%),radial-gradient(ellipse at 65% 35%,#2a6e1f,transparent 55%),radial-gradient(ellipse at 80% 75%,#2a6e1f,transparent 40%),radial-gradient(ellipse at 38% 80%,#25631b,transparent 40%)}
/* cta */
.cta{position:absolute;left:140px;top:4341px;width:920px;height:328px;border-radius:20px;background:radial-gradient(ellipse at 50% 120%,#1f6b1a,transparent 60%),linear-gradient(135deg,#8fcf3a,#3f9a2a 55%,#2a7d20)}
.cta h2{position:absolute;left:0;top:58px;width:920px;text-align:center;font:700 56px var(--head);text-transform:uppercase;letter-spacing:.5px}
.cta p{position:absolute;left:130px;top:142px;width:660px;text-align:center;font:400 14px/23px var(--body);color:#f1f8e8}
/* footer */
.flag-bar{position:absolute;left:140px;top:4712px;width:920px;height:101px;border-radius:10px;background:#222;border:1px solid var(--card-line)}
.flag-bar .row{position:absolute;left:78px;top:41px;display:flex;gap:14px}
.flag-bar .row i{display:block;width:30px;height:19px;border-radius:2px}
.lang{position:absolute;left:720px;top:33px;width:120px;height:36px;border-radius:6px;background:#2e2e2e;display:flex;align-items:center;gap:8px;padding-left:10px;font:400 13px var(--body)}
.lang i{display:block;width:24px;height:15px;border-radius:2px}
.contact{position:absolute;top:4868px;display:flex;align-items:center;gap:12px;font:500 12px/17px var(--body)}
.contact .circ{width:42px;height:42px;border-radius:50%;background:#fff;display:flex;align-items:center;justify-content:center}
.footer-rule{position:absolute;left:140px;top:4965px;width:920px;height:1px;background:#2f2f2f}
.copy{position:absolute;left:140px;top:4990px;font:400 11px var(--body);color:var(--muted)}
.socials{position:absolute;left:912px;top:4983px;display:flex;gap:10px}
.socials i{display:block;width:28px;height:28px;border-radius:50%;border:1.5px solid #666}
.socials i:first-child{background:var(--green);border-color:var(--green)}
</style>
</head>
<body>

<!-- HERO -->
<section class="section hero">
  <div class="hero-photo" role="img" aria-label="Soccer player striking a ball in a floodlit stadium"></div>
  <div class="brand" style="left:105px;top:10px"><span class="brand-dot"></span>Vexorun</div>
  <div class="nav-actions">
    <a class="btn btn-green" style="left:685px;width:203px">Join as Player <span class="arr"><svg width="14" height="14" viewBox="0 0 14 14"><path d="M3 3l4 4-4 4M7 3l4 4-4 4" stroke="#2f7d22" stroke-width="2" fill="none"/></svg></span></a>
    <a class="btn btn-outline" style="left:902px;width:191px">Join as Club <span class="arr"><svg width="14" height="14" viewBox="0 0 14 14"><path d="M3 3l4 4-4 4M7 3l4 4-4 4" stroke="#1c1c1c" stroke-width="2" fill="none"/></svg></span></a>
  </div>
  <h1 class="hero-title">Let the Games Begin &amp;<span>Pick Your Challenge</span></h1>
  <p class="hero-sub">Find Games. Join Events. Connect With Your Sport Community. Anywhere In The World.</p>
  <a class="btn btn-green" style="left:105px;top:370px;width:202px">Join as Player <span class="arr"><svg width="14" height="14" viewBox="0 0 14 14"><path d="M3 3l4 4-4 4M7 3l4 4-4 4" stroke="#2f7d22" stroke-width="2" fill="none"/></svg></span></a>
  <a class="btn btn-outline" style="left:324px;top:370px;width:186px">Join as Club <span class="arr"><svg width="14" height="14" viewBox="0 0 14 14"><path d="M3 3l4 4-4 4M7 3l4 4-4 4" stroke="#1c1c1c" stroke-width="2" fill="none"/></svg></span></a>
  <p class="hero-note">Built For Pickleball &amp; Padel. Expanding To All Sports</p>
  <div class="flags" style="left:100px;top:474px;width:440px;gap:6px 2px">
    <span class="flag"><i class="f-uk"></i>UK</span><span class="flag"><i class="f-es"></i>Spain</span><span class="flag"><i class="f-lu"></i>Luxembourg</span><span class="flag"><i class="f-jp"></i>Japan</span><span class="flag"><i class="f-ru"></i>Russia</span><span class="flag"><i class="f-kr"></i>South Korea</span><span class="flag"><i class="f-ca"></i>Canada</span><span class="flag"><i class="f-us"></i>USA</span><span class="flag"><i class="f-cz"></i>Czech Republic</span><span class="flag"><i class="f-br"></i>Brazil</span>
    <span class="flag"><i class="f-pr"></i>Puerto Rico</span><span class="flag"><i class="f-cr"></i>Costa Rica</span><span class="flag"><i class="f-cn"></i>China</span><span class="flag"><i class="f-in"></i>India</span>
  </div>
  <div class="phones" style="left:890px;top:120px;width:205px;height:468px" role="img" aria-label="App screen showing leagues and competitions"></div>
  <div class="phones" style="left:695px;top:104px;width:222px;height:486px" role="img" aria-label="App home screen with play now, find your match and trending matches"></div>
</section>

<!-- SPORTS -->
<section class="section sports">
  <p class="eyebrow" style="top:76px">Multi-Sport Platform</p>
  <h2 class="title" style="top:98px">Your Sport. Your Rules.</h2>
  <span class="title-bar" style="top:148px"></span>
  <div class="sport-card" style="left:140px"><svg width="44" height="44" viewBox="0 0 44 44"><ellipse cx="26" cy="16" rx="11" ry="12" fill="none" stroke="#9fd236" stroke-width="3"/><path d="M18 25L8 38" stroke="#9fd236" stroke-width="4" stroke-linecap="round"/></svg>Padel</div>
  <div class="sport-card" style="left:327px"><svg width="44" height="44" viewBox="0 0 44 44"><ellipse cx="24" cy="16" rx="12" ry="12" fill="#9fd236"/><path d="M16 25L7 38" stroke="#9fd236" stroke-width="4" stroke-linecap="round"/><circle cx="35" cy="36" r="5" fill="#5fae2e"/></svg>Pickleball</div>
  <div class="sport-card" style="left:514px"><svg width="44" height="44" viewBox="0 0 44 44"><ellipse cx="26" cy="16" rx="11" ry="13" fill="none" stroke="#9fd236" stroke-width="3"/><path d="M18 26L8 38" stroke="#9fd236" stroke-width="4" stroke-linecap="round"/><circle cx="10" cy="10" r="5" fill="#9fd236"/></svg>Tennis</div>
  <div class="sport-card" style="left:701px"><svg width="44" height="44" viewBox="0 0 44 44"><circle cx="22" cy="22" r="17" fill="none" stroke="#9fd236" stroke-width="3"/><path d="M22 14l7 5-3 8h-8l-3-8z" fill="#9fd236"/></svg>Soccer</div>
  <div class="sport-card" style="left:888px"><svg width="44" height="44" viewBox="0 0 44 44"><circle cx="22" cy="22" r="17" fill="#9fd236"/><path d="M5 22h34M22 5v34M10 10c8 6 8 18 0 24M34 10c-8 6-8 18 0 24" stroke="#1c1c1c" stroke-width="2" fill="none"/></svg>Basketball</div>
</section>

<!-- ONE PLACE -->
<section class="section oneplace">
  <p class="eyebrow" style="top:76px">Sport. One Place.</p>
  <h2 class="title" style="top:98px">Everything In Your Sport. One Place.</h2>
  <span class="title-bar" style="top:148px"></span>
  <div class="oneplace-visual" role="img" aria-label="Smiling player holding a phone and a soccer ball beside a row of app screens"></div>
  <h3 class="sub-head" style="left:142px;top:566px">Find Matches</h3>
  <h3 class="sub-head" style="left:778px;top:566px">Now Available In 12</h3>
  <div class="mini-card" style="left:140px;width:289px"><span class="ico"><svg width="26" height="22" viewBox="0 0 26 22"><circle cx="7" cy="6" r="4" fill="#fff"/><circle cx="19" cy="6" r="4" fill="#fff"/><path d="M0 20c0-5 3-8 7-8s7 3 7 8zM12 20c0-5 3-8 7-8s7 3 7 8z" fill="#fff"/></svg></span><p>Match With Players At Your Level</p></div>
  <div class="mini-card" style="left:453px;width:288px"><span class="ico"><svg width="24" height="24" viewBox="0 0 24 24"><rect x="2" y="4" width="20" height="18" rx="2" fill="none" stroke="#fff" stroke-width="2"/><path d="M2 9h20M7 2v4M17 2v4" stroke="#fff" stroke-width="2"/><circle cx="16" cy="16" r="3" fill="#fff"/></svg></span><p>Play Instantly Or Schedule Games</p></div>
  <div class="mini-card" style="left:767px;width:288px">
    <div class="flags" style="left:30px;top:30px;width:240px;gap:6px 0">
      <span class="flag"><i class="f-uk"></i>UK</span><span class="flag"><i class="f-es"></i>Spain</span><span class="flag"><i class="f-lu"></i>Luxembourg</span><span class="flag"><i class="f-jp"></i>Japan</span><span class="flag"><i class="f-ru"></i>Russia</span><span class="flag"><i class="f-kr"></i>South Korea</span>
      <span class="flag"><i class="f-cz"></i>Czech Republic</span><span class="flag"><i class="f-br"></i>Brazil</span><span class="flag"><i class="f-pr"></i>Puerto Rico</span><span class="flag"><i class="f-cr"></i>Costa Rica</span><span class="flag"><i class="f-ca"></i>Canada</span><span class="flag"><i class="f-us"></i>USA</span>
    </div>
  </div>
</section>

<!-- FEATURES -->
<section class="section features">
  <p class="eyebrow" style="top:94px">Platform Features</p>
  <h2 class="title" style="top:116px">Everything You Need To Play</h2>
  <span class="title-bar" style="top:166px"></span>
  <div class="feat" style="left:140px;top:189px"><svg width="56" height="56" viewBox="0 0 56 56"><ellipse cx="34" cy="18" rx="12" ry="14" fill="none" stroke="#fff" stroke-width="3"/><path d="M26 29L12 46" stroke="#fff" stroke-width="4" stroke-linecap="round"/><circle cx="14" cy="16" r="5" fill="#fff"/><circle cx="44" cy="44" r="6" fill="#9fd236"/></svg><h3>Find &amp; Join Games Instantly</h3><p>Browse Open Games Near You Across Multiple Sports. One Tap To Join — No Coordination Headaches, No Group Chats.</p></div>
  <div class="feat" style="left:454px;top:189px"><svg width="56" height="56" viewBox="0 0 56 56"><path d="M14 6h20l10 10v32H14z" fill="#fff"/><circle cx="40" cy="42" r="9" fill="#232323" stroke="#fff" stroke-width="3"/><path d="M40 37v10M35 42h10" stroke="#fff" stroke-width="3"/></svg><h3>Create Games Without Friction</h3><p>Set Up A Game In Seconds. Choose Your Sport, Time, Level, And Let Players Find You. Fill Spots Automatically.</p></div>
  <div class="feat" style="left:768px;top:189px"><svg width="56" height="56" viewBox="0 0 56 56"><path d="M8 18L28 6l20 12z" fill="#fff"/><path d="M12 22h32v24H12z" fill="none" stroke="#fff" stroke-width="3"/><path d="M20 22v24M28 22v24M36 22v24M8 48h40" stroke="#fff" stroke-width="3"/></svg><h3>Club Management Suite</h3><p>Manage Players, Classes, Staff, And Payments In One Dashboard. Turn Empty Court Time Into Revenue.</p></div>
  <div class="feat" style="left:140px;top:425px;padding-top:90px"><svg width="56" height="56" viewBox="0 0 56 56"><circle cx="26" cy="14" r="8" fill="#fff"/><path d="M12 46c0-12 6-18 14-18s14 6 14 18z" fill="#fff"/><circle cx="44" cy="42" r="7" fill="none" stroke="#fff" stroke-width="3"/></svg><h3>Coaches Offering Lessons And Programs</h3><p>Coaches Can List Lessons, Group Programs, And Clinics. Get Paid Directly Through The Platform.</p></div>
  <div class="feat" style="left:454px;top:425px"><svg width="56" height="56" viewBox="0 0 56 56"><circle cx="28" cy="10" r="5" fill="#fff"/><path d="M28 16v8M12 24h32M12 24v8M44 24v8M28 24v8" stroke="#fff" stroke-width="3"/><circle cx="12" cy="38" r="5" fill="#fff"/><circle cx="28" cy="38" r="5" fill="#fff"/><circle cx="44" cy="38" r="5" fill="#fff"/><path d="M6 50h44" stroke="#fff" stroke-width="3"/></svg><h3>Tournaments &amp; Events</h3><p>Organize Inter-Club Tournaments And Community Events. Automated Brackets, Scoring, And Player Registration.</p></div>
  <div class="feat" style="left:768px;top:425px"><svg width="56" height="56" viewBox="0 0 56 56"><rect x="8" y="10" width="34" height="32" rx="3" fill="none" stroke="#fff" stroke-width="3"/><path d="M8 18h34M16 6v8M34 6v8" stroke="#fff" stroke-width="3"/><circle cx="40" cy="40" r="10" fill="#fff"/><text x="40" y="45" text-anchor="middle" font-family="Poppins,sans-serif" font-size="13" font-weight="700" fill="#232323">$</text></svg><h3>Fill Empty Court Time</h3><p>Automate Quick-Created Events To Fill Unused Slots. Every Empty Hour Becomes A Revenue Opportunity For Your Club.</p></div>
  <a class="btn btn-green" style="left:424px;top:672px;width:174px">Join as Player <span class="arr"><svg width="16" height="12" viewBox="0 0 16 12"><path d="M1 6h13M9 1l5 5-5 5" stroke="#2f7d22" stroke-width="2" fill="none"/></svg></span></a>
  <a class="btn btn-white" style="left:615px;top:672px;width:161px">Join as Club <span class="arr"><svg width="16" height="12" viewBox="0 0 16 12"><path d="M1 6h13M9 1l5 5-5 5" stroke="#fff" stroke-width="2" fill="none"/></svg></span></a>
</section>

<!-- HOW IT WORKS -->
<section class="section how">
  <p class="eyebrow" style="top:84px">Simple Process</p>
  <h2 class="title" style="top:106px">How It Works</h2>
  <span class="title-bar" style="top:156px"></span>
  <span class="step-line"></span>
  <div class="step" style="left:125px"><div class="num">01</div><h3>Sign Up Free</h3><p>Create Your Profile In 30 Seconds.<br>No Credit Card Needed.</p></div>
  <div class="step" style="left:375px"><div class="num">02</div><h3>Choose Your Sport</h3><p>Select From Padel, Pickleball,<br>Tennis, Soccer, And More.</p></div>
  <div class="step" style="left:617px"><div class="num">03</div><h3>Find Or Create</h3><p>Join Existing Games Or Create<br>Your Own In Seconds.</p></div>
  <div class="step" style="left:848px"><div class="num">04</div><h3>Play &amp; Grow</h3><p>Meet New Players, Improve<br>Your Game, Build Community.</p></div>
  <a class="btn btn-green" style="left:424px;top:338px;width:174px">Join as Player <span class="arr"><svg width="16" height="12" viewBox="0 0 16 12"><path d="M1 6h13M9 1l5 5-5 5" stroke="#2f7d22" stroke-width="2" fill="none"/></svg></span></a>
  <a class="btn btn-white" style="left:615px;top:338px;width:161px">Join as Club <span class="arr"><svg width="16" height="12" viewBox="0 0 16 12"><path d="M1 6h13M9 1l5 5-5 5" stroke="#fff" stroke-width="2" fill="none"/></svg></span></a>
  <div class="ball" role="img" aria-label="Soccer ball resting on a dark spotlit pitch"></div>
</section>

<!-- BUILT FOR -->
<section class="section builtfor">
  <p class="eyebrow" style="top:84px">Play Sports</p>
  <h2 class="title" style="top:110px">Built For How<br>People Actually Play Sports</h2>
  <div class="role" style="left:143px"><span class="badge"><svg width="40" height="40" viewBox="0 0 40 40"><circle cx="20" cy="10" r="6" fill="none" stroke="#fff" stroke-width="2.5"/><circle cx="9" cy="18" r="4" fill="none" stroke="#fff" stroke-width="2.5"/><circle cx="31" cy="18" r="4" fill="none" stroke="#fff" stroke-width="2.5"/><path d="M8 34c0-8 5-12 12-12s12 4 12 12z" fill="none" stroke="#fff" stroke-width="2.5"/></svg></span><h3>For Players</h3><p>Find Games Instantly.<br>Meet Players.</p></div>
  <div class="role active" style="left:456px"><span class="badge"><svg width="40" height="40" viewBox="0 0 40 40"><rect x="6" y="10" width="24" height="24" rx="2" fill="none" stroke="#fff" stroke-width="2.5"/><path d="M12 10v24M18 10v24M24 10v24" stroke="#fff" stroke-width="2"/><circle cx="32" cy="10" r="6" fill="#fff"/></svg></span><h3>For Clubs</h3><p>Fill Courts. Manage<br>Players, Grow Your Community.</p></div>
  <div class="role" style="left:772px"><span class="badge"><svg width="40" height="40" viewBox="0 0 40 40"><circle cx="20" cy="14" r="6" fill="#fff"/><path d="M10 34c0-8 4-12 10-12s10 4 10 12z" fill="#fff"/><path d="M4 10h6M30 10h6M4 28h5M31 28h5" stroke="#fff" stroke-width="2.5"/></svg></span><h3>For Organizers</h3><p>Run Events, Leagues,<br>And Tournaments Without…</p></div>
</section>

<!-- LAUNCH -->
<section class="section launch">
  <p class="abs" style="left:140px;top:98px;font:500 13px var(--body);color:var(--lime);text-transform:uppercase">Worldwide Century</p>
  <h2 class="launch-title">Launching<br>City By City Worldwide</h2>
  <p class="check" style="top:220px"><i><svg width="8" height="8" viewBox="0 0 8 8"><path d="M1 4l2 2 4-4" stroke="#1c1c1c" stroke-width="1.5" fill="none"/></svg></i>Building The First Global Sports Network.</p>
  <p class="check" style="top:255px"><i><svg width="8" height="8" viewBox="0 0 8 8"><path d="M1 4l2 2 4-4" stroke="#1c1c1c" stroke-width="1.5" fill="none"/></svg></i>Starting With Pickleball &amp; Padel</p>
  <p class="check" style="top:289px"><i><svg width="8" height="8" viewBox="0 0 8 8"><path d="M1 4l2 2 4-4" stroke="#1c1c1c" stroke-width="1.5" fill="none"/></svg></i>Expanding To All Sports</p>
  <div class="flag-box">
    <div class="flags" style="left:20px;top:20px;width:320px;gap:6px 0">
      <span class="flag"><i class="f-uk"></i>UK</span><span class="flag"><i class="f-es"></i>Spain</span><span class="flag"><i class="f-lu"></i>Luxembourg</span><span class="flag"><i class="f-jp"></i>Japan</span><span class="flag"><i class="f-ru"></i>Russia</span><span class="flag"><i class="f-kr"></i>South Korea</span><span class="flag"><i class="f-ca"></i>Canada</span><span class="flag"><i class="f-us"></i>USA</span>
      <span class="flag"><i class="f-cz"></i>Czech Republic</span><span class="flag"><i class="f-br"></i>Brazil</span><span class="flag"><i class="f-pr"></i>Puerto Rico</span><span class="flag"><i class="f-cr"></i>Costa Rica</span>
    </div>
  </div>
  <div class="map" role="img" aria-label="Green world map with location pins on launch cities"></div>
</section>

<!-- CTA -->
<div class="cta">
  <h2>Free To Join. Free To Play.</h2>
  <p>Vexorun Is Free For Players And Coaches To Join. We Only Take A Small Platform Fee On Transactions — Events, Classes, And Subscriptions — So Everyone Wins.</p>
  <a class="btn btn-dark" style="left:298px;top:211px;width:173px">Join as Player <span class="arr"><svg width="16" height="12" viewBox="0 0 16 12"><path d="M1 6h13M9 1l5 5-5 5" stroke="#1c1c1c" stroke-width="2" fill="none"/></svg></span></a>
  <a class="btn btn-white" style="left:487px;top:211px;width:161px">Join as Club <span class="arr"><svg width="16" height="12" viewBox="0 0 16 12"><path d="M1 6h13M9 1l5 5-5 5" stroke="#fff" stroke-width="2" fill="none"/></svg></span></a>
</div>

<!-- FOOTER -->
<div class="flag-bar">
  <div class="row"><i class="f-uk"></i><i class="f-es"></i><i class="f-lu"></i><i class="f-jp"></i><i class="f-ru"></i><i class="f-kr"></i><i class="f-ca"></i><i class="f-us"></i><i class="f-cz"></i><i class="f-br"></i><i class="f-pr"></i><i class="f-cr"></i><i class="f-cn"></i><i class="f-in"></i></div>
  <div class="lang"><i class="f-uk"></i>English <svg width="10" height="6" viewBox="0 0 10 6"><path d="M1 1l4 4 4-4" stroke="#fff" stroke-width="1.5" fill="none"/></svg></div>
</div>
<div class="contact" style="left:203px"><span class="circ"><svg width="18" height="18" viewBox="0 0 24 24"><path d="M6.6 10.8a15 15 0 006.6 6.6l2.2-2.2a1 1 0 011-.25 11.4 11.4 0 003.6.57 1 1 0 011 1V20a1 1 0 01-1 1A17 17 0 013 4a1 1 0 011-1h3.5a1 1 0 011 1 11.4 11.4 0 00.57 3.6 1 1 0 01-.25 1z" fill="#1c1c1c"/></svg></span><span>Call Us<br>+123 555 0147</span></div>
<div class="brand" style="left:466px;top:4858px"><span class="brand-dot" style="width:64px;height:64px"></span>Vexorun</div>
<div class="contact" style="left:815px"><span class="circ"><svg width="18" height="14" viewBox="0 0 18 14"><rect x="1" y="1" width="16" height="12" rx="1.5" fill="#1c1c1c"/><path d="M1 2l8 6 8-6" stroke="#fff" stroke-width="1.5" fill="none"/></svg></span><span>Email<br>info@vexorun.co</span></div>
<span class="footer-rule"></span>
<p class="copy">© 2026 Vexorun.Co. All Rights Reserved.</p>
<div class="socials"><i></i><i></i><i></i><i></i></div>

</body>
</html>
```